Relaunch kvtrelm.com

Nov 12 update: I have a number of very strong submissions to select among - no need for any more, thank you. I am out of the office until Friday, then will be selecting a designer to conclude the project with.

I need someone to review my existing site at WordPress, make it more contemporary and visually appealing while preserving the content, which is quite text-dense, and improve the navigation. For example, if you go to https://kvtrelm.com/claims-handled/ you will see links to dedicated pages for various client groups - I would like those to somehow be evident from the home page.

It would be simpler to keep it at WordPress but I am open to using a different CMS if necessary.

Fluency in Spanish would be useful, since part of the site is in Spanish.

Target Market(s)

Shipowners, vessel operators, ship managers

Industry/Entity Type

Marine insurance / marine transportation

Number of Pages Required

5+ page

Colors

Designer to choose colors to be used in the design.

Requirements
Must have
• Substantially preserve exciting content, but make it more accessible.
Nice to have
• This is an online brochure - we don't sell anything on line. I would like the theme to tie in to the colors in the existing logo, which we will keep.

```html
<!DOCTYPE html>
<html lang="en">
<head>
<meta charset="utf-8">
<title>The Kaverton Company – Average Adjusters</title>
<link href="https://fonts.googleapis.com/css2?family=Poppins:wght@600&family=Raleway:ital,wght@0,300;0,400;0,500;0,600;0,700;1,300;1,400&display=swap" rel="stylesheet">
<style>
:root{
  --brand:#9b1c2a;
  --brand-dark:#8a2228;
  --ink:#222;
  --text:#444;
  --muted:#666;
  --line:#333;
  --footer-bg:#efefef;
  --white:#fff;
}
*{margin:0;padding:0;box-sizing:border-box}
html,body{width:1200px;height:2298px;overflow:hidden;background:var(--white)}
body{position:relative;font-family:"Raleway",sans-serif;color:var(--ink)}
.abs{position:absolute}
a{color:inherit;text-decoration:none}

/* header */
.site-header{left:0;top:0;width:1200px;height:61px;background:var(--white);border-bottom:1px solid #ddd}
.brand-name{left:150px;top:16px;font-size:24px;font-weight:700;color:var(--brand);letter-spacing:1px}
.main-nav{right:150px;top:16px;display:flex;align-items:center;gap:26px;font-size:12.5px;color:#555}
.main-nav .active{color:var(--brand)}
.btn-nav{background:var(--brand);color:var(--white);font-weight:600;padding:7px 14px;border-radius:3px;font-size:12.5px}

/* hero */
.hero{left:0;top:61px;width:1200px;height:600px;
  background:linear-gradient(180deg,#6f6a66 0%,#b59070 28%,#5b6570 48%,#2c3d4c 75%,#1e2c3a 100%)}
.hero-title{left:154px;top:250px;font-family:"Poppins",sans-serif;font-weight:600;font-size:47px;color:var(--white)}
.hero-sub{left:155px;top:334px;font-size:27px;font-weight:500;color:var(--white)}
.hero-btn{left:150px;top:412px;width:165px;height:46px;background:var(--brand);color:var(--white);
  font-weight:700;font-size:18px;display:flex;align-items:center;justify-content:center;border-radius:3px}

/* welcome */
.welcome-kicker{left:0;top:700px;width:1200px;text-align:center;font-style:italic;font-weight:300;font-size:21px;color:var(--brand)}
.welcome-text{left:155px;top:748px;width:900px;font-size:21px;font-weight:400;line-height:31.5px;color:var(--text)}
.welcome-text em{font-weight:300}
.btn-more{left:510px;top:869px;width:180px;height:37px;background:var(--brand);color:var(--white);
  font-size:14.5px;font-weight:500;display:flex;align-items:center;justify-content:center;border-radius:2px}

/* section headings */
.section-title{left:0;width:1200px;text-align:center;font-size:36px;font-weight:500;color:var(--ink)}
.title-rule{height:4px;background:var(--brand)}

/* claims cards */
.claim-card{top:1081px;width:285px;height:284px;border:2px solid var(--line);padding:24px 22px 0 28px}
.claim-card h3{font-size:22px;font-style:italic;font-weight:300;color:var(--brand);margin-bottom:14px}
.claim-card p{font-size:12px;line-height:18px;color:#555;font-weight:400;height:162px}
.claim-card .read-more{display:block;margin-top:12px;font-size:11.5px;font-weight:700;color:var(--brand)}
.slider-arrow{top:1203px}
.dot{top:1389px;width:11px;height:11px;border-radius:50%}

/* staff */
.staff-block{left:0;top:1594px;width:345px;height:323px;background:var(--brand-dark)}
.staff-photo{left:29px;top:1631px;width:375px;height:247px;background:linear-gradient(100deg,#3b4a64 0%,#8a93a3 35%,#dfe2e6 65%,#f4f4f4 100%)}
.staff-card{left:434px;top:1576px;width:615px;height:360px;border:2px solid #5b6b8c;padding:20px 20px 0 21px}
.staff-card h3{font-size:26px;font-weight:500;color:var(--brand-dark);margin-bottom:18px}
.staff-card p{font-size:16.5px;line-height:30px;color:var(--text)}
.btn-learn{display:inline-flex;margin-top:28px;width:165px;height:45px;background:var(--brand-dark);color:var(--white);
  font-size:18px;font-weight:500;align-items:center;justify-content:center;border-radius:2px}

/* footer */
.site-footer{left:0;top:2012px;width:1200px;height:249px;background:var(--footer-bg)}
.footer-heading{font-size:13px;font-weight:700;color:#666;padding-bottom:5px;border-bottom:2px solid var(--brand)}
.footer-links{list-style:none;font-size:12.5px;color:#333}
.footer-links li{height:27px}
.footer-brand{left:520px;top:2100px;width:360px;text-align:center;font-size:46px;font-weight:700;color:var(--brand);letter-spacing:3px}
.contact-row{display:flex;align-items:flex-start;gap:8px;font-size:12px;color:#777;line-height:18px}
.copy-bar{left:0;top:2261px;width:1200px;height:37px;background:var(--brand-dark)}
.copy-text{left:150px;top:2274px;font-size:9px;color:var(--white)}
.social{top:2269px;width:22px;height:22px;border:2px solid var(--white);border-radius:50%}
</style>
</head>
<body>

<header class="abs site-header">
  <div class="abs brand-name">KVTRELM</div>
  <nav class="abs main-nav">
    <a class="active">Home</a>
    <a>Claims Handled</a>
    <a>General Average</a>
    <a>Staff</a>
    <a>Resources</a>
    <a>Español</a>
    <a class="btn-nav">Contact Us</a>
  </nav>
</header>

<section class="abs hero" role="img" aria-label="Container ship sailing on open sea at sunset"></section>
<h1 class="abs hero-title">The Kaverton Company</h1>
<p class="abs hero-sub">Average adjusters &amp; marine insurance consultants</p>
<a class="abs hero-btn">Contact Us</a>

<p class="abs welcome-kicker">Welcome to the Kaverton Company</p>
<p class="abs welcome-text">The Kaverton Company is a leading, independent average adjuster, in operation since 1998. We take pride in the <em>speed</em> of our response, the <em>accuracy</em> of our work, the <em>reasonableness</em> of our fees and the <em>professional standards</em> we uphold.</p>
<a class="abs btn-more">MORE ABOUT US</a>

<h2 class="abs section-title" style="top:970px">Claims Handled</h2>
<div class="abs title-rule" style="left:465px;top:1014px;width:271px"></div>

<svg class="abs slider-arrow" style="left:27px" width="42" height="42" viewBox="0 0 42 42" aria-hidden="true">
  <circle cx="21" cy="21" r="19.5" fill="none" stroke="#333" stroke-width="2"/>
  <path d="M24 13 L16 21 L24 29" fill="none" stroke="#333" stroke-width="2.5"/>
</svg>
<svg class="abs slider-arrow" style="left:1140px" width="42" height="42" viewBox="0 0 42 42" aria-hidden="true">
  <circle cx="21" cy="21" r="19.5" fill="none" stroke="var(--brand)" stroke-width="2"/>
  <path d="M18 13 L26 21 L18 29" fill="none" stroke="var(--brand)" stroke-width="2.5"/>
</svg>

<article class="abs claim-card" style="left:150px">
  <h3>For Owners</h3>
  <p>All average adjusters are not created equal. Of particular relevance in the US, if your insurance brokers have average adjusters on staff, you also have the option of instructing independent average adjusters, and we will work in close cooperation with your brokers to ensure a prompt and accurate claim outcome.</p>
  <a class="read-more">READ MORE</a>
</article>
<article class="abs claim-card" style="left:457px">
  <h3>For Insurance Brokers</h3>
  <p>The Kaverton Company is ideally suited to assisting independent brokers in developing new business and servicing and retaining existing business. Not every insured wants to deal with the mega brokers, but they might like the idea of the all-round claims service offered by staff average adjusters.</p>
  <a class="read-more">READ MORE</a>
</article>
<article class="abs claim-card" style="left:765px">
  <h3>For Underwriters</h3>
  <p>Specialist opinions: How often have you turned to an attorney for an opinion on coverage and quantum only to find that your Insured interprets this as an adversarial gesture? He then appoints his own attorney and, at best, a client is lost, and at worst a claim for which you had every intention of finding a solution ends up in litigation.</p>
  <a class="read-more">READ MORE</a>
</article>

<span class="abs dot" style="left:585px;background:var(--brand-dark)"></span>
<span class="abs dot" style="left:604px;background:#444"></span>

<h2 class="abs section-title" style="top:1463px">Meet Our Staff</h2>
<div class="abs title-rule" style="left:476px;top:1508px;width:248px"></div>

<div class="abs staff-block"></div>
<div class="abs staff-photo" role="img" aria-label="Portrait of a senior adjuster in a suit holding a leather folder"></div>
<article class="abs staff-card">
  <h3>Martin R. Kaverton</h3>
  <p>Martin Kaverton began his career in Rotterdam in 1979 with an international average adjusting company. He moved to Boston in 1982 and has lived here ever since. In 1988, he became a Full Member, by examination, of the Guild of Marine Claims Assessors.<br>In 1997 he joined a major Nordic marine insurer and opened a Boston office for them.</p>
  <a class="btn-learn">Learn More</a>
</article>

<footer class="abs site-footer"></footer>
<div class="abs" style="left:150px;top:2040px">
  <div class="footer-heading" style="display:inline-block">QUICK NAVIGATION</div>
  <ul class="footer-links" style="margin-top:14px">
    <li>Home</li><li>Claims Handled</li><li>General Average</li><li>Staff</li><li>Resources</li><li>Español</li>
  </ul>
</div>
<div class="abs" style="left:322px;top:2040px">
  <div class="footer-heading" style="display:inline-block">COMPANY INFORMATION</div>
  <ul class="footer-links" style="margin-top:14px">
    <li>Search</li><li>Frequently Asked Questions (FAQ)</li><li>Privacy</li><li>Terms of Service</li>
  </ul>
</div>
<div class="abs footer-brand">KVTRELM</div>
<div class="abs" style="left:890px;top:2040px;width:170px">
  <div class="footer-heading" style="display:inline-block">CONTACT US</div>
  <div class="contact-row" style="margin-top:14px">
    <svg width="22" height="22" viewBox="0 0 22 22" aria-hidden="true"><circle cx="11" cy="11" r="10" fill="none" stroke="#888" stroke-width="1.5"/><path d="M7.5 6.5 l2 -0.5 l1 2.5 l-1.3 1 a6 6 0 0 0 3 3 l1-1.3 l2.5 1 l-0.5 2 c-4 0.5-8-3.5-7.7-7.7z" fill="#888"/></svg>
    <span style="padding-top:2px">+1 (555) 014-2290</span>
  </div>
  <div class="contact-row" style="margin-top:11px">
    <svg width="22" height="22" viewBox="0 0 22 22" aria-hidden="true"><circle cx="11" cy="11" r="10" fill="none" stroke="#888" stroke-width="1.5"/><rect x="6" y="7.5" width="10" height="7" fill="none" stroke="#888" stroke-width="1.3"/><path d="M6 7.5 l5 4 l5-4" fill="none" stroke="#888" stroke-width="1.3"/></svg>
    <span style="padding-top:2px">info@kvtrelm.com</span>
  </div>
  <div class="contact-row" style="margin-top:11px">
    <svg width="22" height="22" viewBox="0 0 22 22" aria-hidden="true" style="flex:none"><circle cx="11" cy="11" r="10" fill="none" stroke="#888" stroke-width="1.5"/><path d="M11 17 c-3-3.5-4-5.5-4-7 a4 4 0 0 1 8 0 c0 1.5-1 3.5-4 7z" fill="none" stroke="#888" stroke-width="1.3"/><circle cx="11" cy="10" r="1.4" fill="#888"/></svg>
    <span>1870 Harbor Ridge Road, Millbrook Falls, NY 10999, USA</span>
  </div>
</div>

<div class="abs copy-bar"></div>
<p class="abs copy-text">Copyright 2024 © The Kaverton Company – KVTRELM- All rights Reserved</p>
<span class="abs social" style="left:995px" aria-label="Social profile"></span>
<span class="abs social" style="left:1026px" aria-label="Social profile"></span>

</body>
</html>
```